Präsentationsvorlagen/Workbook für Coaching - Yoga - Training
Zielgruppe
Coaching - Yoga - Training, d.h. Yogaunterricht, Einzelcoaching, Seminare und Workshops rund um das Thema Stress/Resilienz/Achtsamkeit
Zielgruppe sind einerseits überwiegend Frauen, aber auch Firmenkunden, die für ihre Mitarbeiter Seminare und Yoga anbieten.
Aufgabenstellung
Ich benötige einen professionellen ppt Auftritt für Präsentationen/Workbooks mit meinen Firmenfarben (grau, weiß, rosa, beige) in den mein Logo integriert ist.
Das Design sollte dem Thema entsprechend 'warm' sein aber die nötige Professionalität für Firmenkunden ausstrahlen.

```html
<!DOCTYPE html>
<html lang="de">
<head>
<meta charset="utf-8">
<title>Coaching – Yoga – Training · Präsentationsvorlagen</title>
<link rel="stylesheet" href="https://fonts.googleapis.com/css2?family=Cinzel:wght@400;700&family=Source+Sans+3:wght@400;600&display=swap">
<style>
  :root {
    --stage: #ecebec;
    --berry: #a3456f;
    --berry-deep: #8e3a61;
    --white: #ffffff;
    --blush: #f6eef2;
    --lavender: #e3dcec;
    --grey-text: #6b5a63;
    --shadow: 0 6px 18px rgba(60, 40, 55, 0.12);
  }
  * { box-sizing: border-box; margin: 0; padding: 0; }
  html, body { width: 1200px; height: 622px; overflow: hidden; background: var(--stage); }
  .deck { position: relative; width: 1200px; height: 622px; }
  .slide {
    position: absolute; width: 360px; height: 203px; overflow: hidden;
    background: var(--white); box-shadow: var(--shadow);
  }
  .slide svg.bg { position: absolute; inset: 0; width: 100%; height: 100%; }
  .slide--cover { left: 30px; top: 93px; }
  .slide--title { left: 420px; top: 93px; }
  .slide--training { left: 810px; top: 93px; }
  .slide--coaching { left: 225px; top: 326px; }
  .slide--yoga { left: 615px; top: 326px; }

  .content { position: absolute; }
  .heading { font-family: "Cinzel", serif; font-weight: 700; font-size: 15px; letter-spacing: .5px; color: var(--berry); }
  .subheading { font-family: "Cinzel", serif; font-size: 7.5px; line-height: 1.25; color: var(--berry); margin-top: 3px; }
  .body-text { font-family: "Source Sans 3", sans-serif; font-size: 5.6px; line-height: 1.5; color: var(--berry); margin-top: 10px; }
  .on-berry .heading, .on-berry .subheading, .on-berry .body-text { color: var(--white); }

  .brand-mark {
    position: absolute; top: 9px; right: 10px; display: flex; align-items: center; gap: 3px;
    font-family: "Cinzel", serif; font-size: 5.5px; font-weight: 700; color: var(--berry);
  }
  .brand-mark .dot { width: 9px; height: 9px; border-radius: 50%; border: 1px solid var(--berry); }

  .cover-name {
    position: absolute; left: 0; right: 0; top: 50%; transform: translateY(-50%);
    text-align: center; font-family: "Cinzel", serif; font-weight: 700; font-size: 18px;
    letter-spacing: 1px; color: var(--white);
  }
  .title-block { position: absolute; left: 0; right: 0; top: 96px; text-align: center; }
  .title-block .services { font-family: "Cinzel", serif; font-size: 13px; color: #3d3338; letter-spacing: .5px; }
  .title-block .person { font-family: "Cinzel", serif; font-weight: 700; font-size: 10.5px; color: var(--berry); margin-top: 4px; }
</style>
</head>
<body>
<main class="deck">

  <!-- Cover -->
  <section class="slide slide--cover">
    <svg class="bg" viewBox="0 0 360 203" preserveAspectRatio="none">
      <defs>
        <linearGradient id="cover-sky" x1="0" y1="0" x2="0" y2="1">
          <stop offset="0" stop-color="#7d7191"/>
          <stop offset=".45" stop-color="#d99a9c"/>
          <stop offset=".62" stop-color="#efb27f"/>
          <stop offset=".75" stop-color="#5a4f5c"/>
          <stop offset="1" stop-color="#2a2428"/>
        </linearGradient>
      </defs>
      <rect width="360" height="203" fill="url(#cover-sky)" role="img" aria-label="Foto: Frau in Yogahaltung als Silhouette vor einem Sonnenuntergang am Meer"/>
    </svg>
    <div class="cover-name">Lena Hartwig</div>
  </section>

  <!-- Title -->
  <section class="slide slide--title">
    <svg class="bg" viewBox="0 0 360 203" preserveAspectRatio="none">
      <path d="M200 0 C 230 40, 290 80, 360 70 L360 0 Z" fill="var(--blush)"/>
      <path d="M0 150 C 60 175, 150 190, 240 165 C 290 150, 330 160, 360 178 L360 203 L0 203 Z" fill="#ead9e1"/>
      <path d="M0 190 C 80 175, 160 160, 240 158 C 300 157, 340 170, 360 180 L360 203 L0 203 Z" fill="var(--berry)"/>
    </svg>
    <div class="brand-mark"><span class="dot"></span>Lena Hartwig</div>
    <div class="title-block">
      <p class="services">Coaching - Yoga - Training</p>
      <p class="person">Lena Hartwig</p>
    </div>
  </section>

  <!-- Training -->
  <section class="slide slide--training">
    <svg class="bg" viewBox="0 0 360 203" preserveAspectRatio="none">
      <defs>
        <linearGradient id="lake-dawn" x1="0" y1="0" x2="0" y2="1">
          <stop offset="0" stop-color="#e9c2b5"/>
          <stop offset=".35" stop-color="#d88c6a"/>
          <stop offset=".55" stop-color="#6e5a63"/>
          <stop offset="1" stop-color="#2b2a36"/>
        </linearGradient>
      </defs>
      <rect width="160" height="203" fill="url(#lake-dawn)" role="img" aria-label="Foto: Ruderboot auf einem nebligen See bei Sonnenaufgang"/>
      <path d="M112 0 C 150 50, 100 130, 132 203 L360 203 L360 0 Z" fill="var(--white)"/>
    </svg>
    <div class="brand-mark"><span class="dot"></span>Lena Hartwig</div>
    <div class="content" style="left:150px; top:40px; width:190px;">
      <h2 class="heading">Training</h2>
      <p class="subheading">_ Mit Freude Neues erlernen!</p>
      <p class="body-text">Als erfahrene Trainerin begleite ich Menschen dabei, Neues mit Freude zu lernen. Meine Seminare sind praxisnah, lebendig und auf die Zielgruppe abgestimmt.</p>
    </div>
  </section>

  <!-- Coaching -->
  <section class="slide slide--coaching on-berry">
    <svg class="bg" viewBox="0 0 360 203" preserveAspectRatio="none">
      <defs>
        <linearGradient id="sea-dusk" x1="0" y1="0" x2="0" y2="1">
          <stop offset="0" stop-color="#6f78a8"/>
          <stop offset=".4" stop-color="#c59bb4"/>
          <stop offset=".55" stop-color="#e7a7a2"/>
          <stop offset=".7" stop-color="#7a6485"/>
          <stop offset="1" stop-color="#231d33"/>
        </linearGradient>
      </defs>
      <rect width="140" height="203" fill="url(#sea-dusk)" role="img" aria-label="Foto: ruhiges Meer in der Abenddämmerung mit Bergen am Horizont"/>
      <path d="M118 0 C 95 50, 135 110, 112 203 L360 203 L360 0 Z" fill="var(--berry)"/>
    </svg>
    <div class="content" style="left:150px; top:38px; width:190px;">
      <h2 class="heading">Coaching</h2>
      <p class="subheading">_ Zurück zur Selbstfürsorge<br>und Selbstbestimmtheit</p>
      <p class="body-text">Wo stehst Du heute? Und wo möchtest Du hin? Coaching ist ein lösungsorientierter Prozess, der Dir hilft, neue Blickwinkel zu entdecken und Deine eigenen Ressourcen zu stärken.</p>
    </div>
  </section>

  <!-- Yoga -->
  <section class="slide slide--yoga">
    <svg class="bg" viewBox="0 0 360 203" preserveAspectRatio="none">
      <defs>
        <linearGradient id="yoga-haze" x1="0" y1="0" x2="0" y2="1">
          <stop offset="0" stop-color="#c9bfe0"/>
          <stop offset=".6" stop-color="#e4cfe0"/>
          <stop offset="1" stop-color="#f0dbe3"/>
        </linearGradient>
      </defs>
      <rect width="150" height="203" fill="url(#yoga-haze)" role="img" aria-label="Foto: Silhouette einer Frau in einer Balance-Yogahaltung vor hellem Himmel"/>
      <path d="M100 0 C 140 60, 90 120, 130 203 L360 203 L360 0 Z" fill="var(--blush)"/>
    </svg>
    <div class="brand-mark"><span class="dot"></span>Lena Hartwig</div>
    <div class="content" style="left:150px; top:38px; width:190px;">
      <h2 class="heading">Yoga</h2>
      <p class="subheading">_ Innere Ruhe und Steigerung<br>des Wohlbefindens</p>
      <p class="body-text">„Yoga ist das zur Ruhe kommen der Gedanken im Geist“ – so beschreibt es die alte Lehre. In meinen Kursen verbinde ich Körperübungen, Atem und Meditation zu einer sanften Praxis.</p>
    </div>
  </section>

</main>
</body>
</html>
```